Business card design needed

We need a new business card design to re launch my carpentry business. Could include double sided card with list of services provided.
Kitchens, bathrooms, decks, pergolas, window replacements, timber floor installation, owner builder assistance and general carpentry.
Would like an eye catching card that becons to be read in bright colors that has a logo that could be also used on clothing vehicle sinage etc
Preferably in blues and reds we live near beach so maybe some type of Beecher feel
Target Market(s)
The target market of my business would be mainly individuals requiring professional carpentry services not just a handy man. The renovation market plays a big part of my business
Industry/Entity Type
Carpentry
Contact Information for Business Card
Carpenter & joiner
Rob Pelham
Inverloch
gilda_robbo@tarnmail.com
0439862150
Look and feel
Each slider illustrates characteristics of the customer's brand and the style your logo design should communicate.

```html
<!DOCTYPE html>
<html lang="en">
<head>
<meta charset="utf-8">
<title>Carpenter &amp; joiner Rob Pelham – business card</title>
<link rel="stylesheet" href="https://fonts.googleapis.com/css2?family=Source+Sans+3:wght@400;600&display=swap">
<style>
  :root {
    --backdrop: #e9e6e2;
    --card: #ffffff;
    --ink: #2b2b2b;
    --ink-soft: #4a4a4a;
    --accent: #d21f26;
    --card-shadow: 0 10px 30px rgba(0,0,0,0.18);
  }
  * { box-sizing: border-box; margin: 0; padding: 0; }
  html, body {
    width: 1200px; height: 1200px; overflow: hidden;
    background: var(--backdrop);
    font-family: "Source Sans 3", "Myriad Pro", sans-serif;
    color: var(--ink);
  }
  .sheet {
    width: 1200px; height: 1200px;
    display: flex; flex-direction: column;
    align-items: center; justify-content: center; gap: 50px;
  }
  .card {
    position: relative;
    width: 860px; height: 520px;
    background: var(--card);
    box-shadow: var(--card-shadow);
    overflow: hidden;
  }

  /* Services side */
  .card--services .brand {
    position: absolute; left: 70px; top: 200px;
    display: flex; align-items: center; gap: 12px;
  }
  .brand-dot {
    width: 22px; height: 22px; border-radius: 50%;
    background: var(--accent);
  }
  .brand-name {
    font-weight: 600; font-size: 40px; color: var(--accent);
    letter-spacing: 0.5px;
  }
  .card--services .divider {
    position: absolute; left: 290px; top: 50px;
    width: 2px; height: 420px; background: var(--accent);
  }
  .services {
    position: absolute; left: 340px; top: 90px;
    display: grid; grid-template-columns: 240px 240px; column-gap: 30px;
    list-style: none; font-size: 22px; line-height: 1.2; color: var(--ink-soft);
  }
  .services-col { list-style: none; }
  .card--services .trade-line {
    position: absolute; left: 340px; bottom: 80px;
    font-size: 38px; color: var(--ink);
  }

  /* Contact side */
  .card--contact .brand {
    position: absolute; left: 0; right: 0; top: 80px;
    display: flex; justify-content: center; align-items: center; gap: 14px;
  }
  .card--contact .brand-name { font-size: 64px; }
  .card--contact .brand-dot { width: 30px; height: 30px; }
  .card--contact .trade-line {
    position: absolute; left: 90px; top: 230px;
    font-size: 44px; color: var(--ink);
  }
  .card--contact .rule {
    position: absolute; left: 90px; right: 90px; top: 300px;
    height: 3px; background: var(--accent);
  }
  .contact {
    position: absolute; left: 0; right: 0; top: 360px;
    text-align: center; font-size: 22px; line-height: 1.4; color: var(--ink);
    font-style: normal;
  }
</style>
</head>
<body>
<main class="sheet">
  <section class="card card--services" aria-label="Card back: services">
    <div class="brand"><span class="brand-dot"></span><span class="brand-name">Pelham</span></div>
    <div class="divider"></div>
    <div class="services">
      <ul class="services-col">
        <li>Kitchens,</li>
        <li>decks,</li>
        <li>window replacements,</li>
        <li>owner builder assistance and</li>
      </ul>
      <ul class="services-col">
        <li>bathrooms,</li>
        <li>pergolas,</li>
        <li>timber floor installation,</li>
        <li>general carpentry.</li>
      </ul>
    </div>
    <p class="trade-line">Carpenter &amp; joiner Rob Pelham</p>
  </section>

  <section class="card card--contact" aria-label="Card front: contact">
    <div class="brand"><span class="brand-dot"></span><span class="brand-name">Pelham</span></div>
    <p class="trade-line">Carpenter &amp; joiner Rob Pelham</p>
    <div class="rule"></div>
    <address class="contact">
      <div class="contact-email">gilda_robbo@tarnmail.com</div>
      <div class="contact-phone">0439862150</div>
    </address>
  </section>
</main>
</body>
</html>
```